Redesign Canvas Art E-Commerce Website

Help! I hired a couple of companies on Tasklyn.com to build and design an e-commerce website for me. After three long and painful months, I have one that I believe is functional on the back-end, but aesthetically on the front end is a mess.

We are a small family business that will take your digital photo and manipulate it into a digitally created oil, watercolor or impressionist style pieces of artwork that we print on museum quality, gallery grade canvas and ship to the customer, ready to hang.

We are looking to create an e-commerce website where a customer can choose their art style, upload a photo, choose their canvas size and orientation (horizontal or vertical) and checkout. Within 48 hours, we will send them back a proof of their newly created, customized artwork for them to approve or not approve. If they approve, we print, package and ship them the product. If they do not approve, we offer unlimited revisions until they are happy.

As I mentioned, the back end functionality is already there, just need design help. No coding required

Here is a link to the development page that they created: https://brushvalepicture.com/development/

As you can see, it looks off...doesnt line up properly, wasted space, weird font. Feel free to either correct the homepage they created or design an entirely new page. I am attaching some examples of before and after photos of artwork for reference. I also think the testimonials page and shop page can use a little style. The content is there and accurate, it just doesn't look pretty. Please keep in mind that our customers will probably not be very tech savvy. The customers will probably be sending us pics of kids, grandkids, pets, family portraits, vacation photos, etc.

Here is one of our competitors - www.pelmorastudio.com
Their website looks clean and inviting.

Thank you in advance! Im looking forward to seeing the results. I am including our logo in the attachments (I do not have it in a vector file, just a jpeg)

Target Market(s)

Non tech-savvy indiduals, 30-70 years old

Industry/Entity Type

Please look at https://brushvalepicture.com/development/ to see various pages and what the other designers did

Number of Pages Required

1 page

Requirements
Must have
• Verbiage on pages leave "as is" but feel free to change styles. Would like to keep existing four categories on homepage
Nice to have
• Warm and inviting homepage that evokes emotion

```html
<!DOCTYPE html>
<html lang="en">
<head>
<meta charset="utf-8">
<title>Brushvale Prints – Turn Your Digital Photos Into Wall Art</title>
<link href="https://fonts.googleapis.com/css2?family=Berkshire+Swash&family=Roboto:wght@400;500;700&display=swap" rel="stylesheet">
<style>
:root{
  --orange:#e8501e;
  --orange-deep:#d8401a;
  --green:#2e7d3a;
  --ink:#222;
  --text:#555;
  --muted:#777;
  --hero-bg:#f2f0e9;
  --about-bg:#fbefed;
  --footer-bg:#2b2b2b;
  --white:#fff;
}
*{box-sizing:border-box;margin:0;padding:0}
html,body{width:1200px;height:4289px;overflow:hidden;background:var(--white);font-family:'Roboto',sans-serif;color:var(--ink)}
.page{position:relative;width:1200px;height:4289px}
.abs{position:absolute}
.script{font-family:'Berkshire Swash',cursive;font-weight:400}
.btn{position:absolute;display:flex;align-items:center;justify-content:center;background:var(--orange);color:var(--white);font-size:15px;font-weight:500;text-transform:uppercase;border-radius:3px;box-shadow:0 3px 6px rgba(0,0,0,.15)}

/* header */
.brand{position:absolute;display:flex;align-items:center;gap:10px;font-weight:700;font-size:30px;color:var(--ink)}
.brand .dot{width:22px;height:22px;border-radius:50%;background:var(--orange)}
.nav{position:absolute;left:373px;top:34px;display:flex;font-size:15px;color:#333}
.nav span{position:absolute;white-space:nowrap}
.cart{position:absolute;left:1043px;top:28px}

/* hero */
.hero{left:20px;top:92px;width:1160px;height:611px;background:var(--hero-bg)}
.hero h1{position:absolute;left:113px;top:250px;font-size:60px;line-height:62px;color:#1d1d1d}
.hero h1 em{font-style:normal;color:var(--green)}
.hero-photo{left:590px;top:150px;width:590px;height:553px;background:radial-gradient(ellipse at 55% 45%,#c9a98a 0%,#8fa3a0 45%,#dcd8cd 80%,var(--hero-bg) 100%);border-radius:48% 45% 0 0}

/* section titles */
.title{position:absolute;left:0;width:1200px;text-align:center;font-size:38px;color:#1d1d1d}

/* categories */
.cat{position:absolute;width:230px;text-align:center}
.cat .ring{width:230px;height:230px;border-radius:50%;border:2px solid var(--green);padding:6px;box-shadow:inset 0 0 0 2px #c0392b}
.cat .ring div{width:100%;height:100%;border-radius:50%}
.cat h3{margin-top:14px;font-size:20px;color:#222}
.getstarted{display:inline-flex;align-items:center;gap:8px;margin-top:6px;font-size:14px;font-weight:700;color:var(--orange);text-transform:uppercase}
.arrow-dot{width:13px;height:13px;border-radius:50%;background:var(--orange);display:inline-flex;align-items:center;justify-content:center}

/* about */
.about{left:20px;top:1260px;width:1160px;height:630px;background:var(--about-bg)}
.about-intro{position:absolute;left:0;top:1362px;width:1200px;text-align:center;font-size:15px;color:#333}
.about-photo{left:138px;top:1422px;width:402px;height:408px;border-radius:16px;border:4px solid #111;background:linear-gradient(160deg,#4a2a16 0%,#9a6a3e 40%,#d9cfa0 70%,#5d3a1e 100%)}
.about-text{position:absolute;left:592px;top:1418px;width:488px;font-size:14.6px;line-height:26px;color:var(--text);text-align:justify}
.about-text p{margin-bottom:10px}

/* why us */
.feature{position:absolute;width:300px;text-align:center}
.feature .icon{width:115px;height:115px;border-radius:50%;margin:0 auto;display:flex;align-items:center;justify-content:center}
.feature h3{font-size:19px;font-weight:500;margin-top:30px;color:#222}
.feature p{font-size:14.5px;line-height:24px;color:var(--text);margin-top:20px}
.readmore{display:inline-flex;align-items:center;gap:8px;margin-top:12px;font-size:14px;font-weight:700;color:var(--orange-deep);text-transform:uppercase}
.feature-card{left:433px;top:2063px;width:336px;height:370px;background:var(--white);border-radius:24px;box-shadow:0 6px 24px rgba(0,0,0,.12);border-bottom:4px solid var(--orange)}

/* testimonials */
.testimonials{left:20px;top:2519px;width:1160px;height:528px;background:linear-gradient(135deg,#e9541f 0%,#dc3f18 60%,#c9361a 100%)}
.testimonials .title{color:var(--white)}
.review{position:absolute;top:2722px;width:390px;height:238px;background:var(--white);border-radius:26px;padding:26px 24px 0 44px;box-shadow:0 6px 18px rgba(0,0,0,.15)}
.review h4{font-size:16px;font-weight:500;color:#222}
.review .meta{display:flex;gap:28px;align-items:center;margin-top:8px;font-size:13px;color:#555}
.stars{display:flex;gap:2px}
.review p{margin-top:8px;font-size:13.4px;line-height:24px;color:#888;text-align:justify}
.slide-arrow{position:absolute;top:2838px;width:40px;height:40px;border-radius:50%;border:2px solid var(--white);display:flex;align-items:center;justify-content:center}

/* gallery */
.gallery-main{left:111px;top:3250px;width:680px;height:450px;background:linear-gradient(135deg,#6b4a2a 0%,#b5702c 35%,#d9944a 55%,#3c2a1c 100%)}
.gallery-thumb{left:810px;width:279px;height:142px}

/* footer */
.footer{left:0;top:3873px;width:1200px;height:416px;background:var(--footer-bg);color:var(--white)}
.footer .brand{color:var(--white)}
.social{position:absolute;top:4020px;width:30px;height:30px;border-radius:50%;border:1.5px solid #1ba0d8}
.fcol{position:absolute;top:3925px;font-size:15px;color:#ddd}
.fcol h4{font-size:17px;font-weight:500;color:var(--white);margin-bottom:20px}
.fcol li{list-style:none;margin-bottom:12px;font-size:15px}
.contact-item{display:flex;gap:14px;margin-bottom:18px;font-size:14px;line-height:18px}
.contact-item b{display:block;font-size:12px;font-weight:700}
.footer-rule{left:111px;top:4210px;width:978px;height:1px;background:#555}
.copyright{position:absolute;left:0;top:4240px;width:1200px;text-align:center;font-size:15px;color:#eee}
.to-top{left:1105px;top:4165px;width:36px;height:36px;border-radius:50%;background:#1ba0d8;display:flex;align-items:center;justify-content:center}
</style>
</head>
<body>
<div class="page">

  <!-- header -->
  <div class="brand" style="left:105px;top:24px"><span class="dot"></span>Brushvale</div>
  <nav class="nav">
    <span style="left:0">Home</span>
    <span style="left:72px">Shop</span>
    <span style="left:137px">Testimonials</span>
    <span style="left:256px">About Us</span>
    <span style="left:349px">FAQs</span>
    <span style="left:416px">My Orders</span>
    <span style="left:517px">Contact Us
      <svg width="14" height="10" viewBox="0 0 14 10" style="margin-left:8px"><path d="M2 2l5 5 5-5" fill="none" stroke="#333" stroke-width="2.5"/></svg>
    </span>
  </nav>
  <svg class="cart" width="40" height="36" viewBox="0 0 40 36" aria-label="Cart">
    <path d="M2 6h6l5 18h20l4-13H10" fill="none" stroke="#666" stroke-width="2.4"/>
    <circle cx="15" cy="30" r="3" fill="#666"/><circle cx="30" cy="30" r="3" fill="#666"/>
    <circle cx="35" cy="5" r="5" fill="var(--green)"/>
    <text x="35" y="8" font-size="8" fill="#fff" text-anchor="middle" font-family="Roboto">0</text>
  </svg>

  <!-- hero -->
  <section class="abs hero">
    <h1 class="script" style="left:93px;top:158px">Turn Your Digital<br>Photos Into <em>One of</em><br><em>a Kind</em> Wall Art</h1>
  </section>
  <div class="abs hero-photo" role="img" aria-label="Painted portrait of a laughing grandmother riding piggyback on her grandfather"></div>
  <div class="btn" style="left:113px;top:487px;width:155px;height:50px">Learn More</div>

  <!-- categories -->
  <h2 class="title script" style="top:782px">Our Categories</h2>
  <div class="cat" style="left:120px;top:880px">
    <div class="ring"><div role="img" aria-label="Oil style wedding couple painting" style="background:linear-gradient(160deg,#3d5a2a,#a6895f,#e6dcc8)"></div></div>
    <h3 class="script">Oil</h3>
    <span class="getstarted">Get Started <span class="arrow-dot"><svg width="7" height="7" viewBox="0 0 7 7"><path d="M2 1l3 2.5L2 6" fill="none" stroke="#fff" stroke-width="1.5"/></svg></span></span>
  </div>
  <div class="cat" style="left:366px;top:880px">
    <div class="ring"><div role="img" aria-label="Watercolor mother and baby painting" style="background:linear-gradient(160deg,#f6e2da,#e9bfae,#fbf3ef)"></div></div>
    <h3 class="script">Watercolor</h3>
    <span class="getstarted">Get Started <span class="arrow-dot"><svg width="7" height="7" viewBox="0 0 7 7"><path d="M2 1l3 2.5L2 6" fill="none" stroke="#fff" stroke-width="1.5"/></svg></span></span>
  </div>
  <div class="cat" style="left:611px;top:880px">
    <div class="ring"><div role="img" aria-label="Impressionist painting of a traveller at a Venice canal" style="background:linear-gradient(180deg,#9fc6d8,#2f8f8a,#c0392b)"></div></div>
    <h3 class="script">Impressionist</h3>
    <span class="getstarted">Get Started <span class="arrow-dot"><svg width="7" height="7" viewBox="0 0 7 7"><path d="M2 1l3 2.5L2 6" fill="none" stroke="#fff" stroke-width="1.5"/></svg></span></span>
  </div>
  <div class="cat" style="left:857px;top:880px">
    <div class="ring"><div role="img" aria-label="Digital photo of two children eating ice cream" style="background:linear-gradient(160deg,#d8d4c8,#c9a07a,#5aa8c8)"></div></div>
    <h3 class="script">Digital Photo</h3>
    <span class="getstarted">Get Started <span class="arrow-dot"><svg width="7" height="7" viewBox="0 0 7 7"><path d="M2 1l3 2.5L2 6" fill="none" stroke="#fff" stroke-width="1.5"/></svg></span></span>
  </div>

  <!-- about -->
  <section class="abs about"></section>
  <h2 class="title script" style="top:1304px">About Us</h2>
  <p class="about-intro">At Brushvale Prints, we take your digital photo and turn it into a one-of-a-kind piece of artwork!</p>
  <div class="abs about-photo" role="img" aria-label="Oil painted portrait of a bride holding a bouquet"></div>
  <div class="about-text">
    <p>The process couldn't be any easier. Simply upload your photo, choose your art style and size, and let our team of skilled digital artists do the rest. Do you want to put your digital photo on canvas without an art style? No problem! Just choose the "Digital Photo/Retouching" category and upload your photo. We can print your photo "as is" or do some minor retouching (e.g. remove objects, enhance colors, lighten photo, etc)</p>
    <p>You will receive a proof in your email to approve within 1-2 days. Once approved, your customized artwork will be transferred to canvas and shipped from our design studio in Florida.</p>
    <p>Brushvale Prints art makes a great gift for just about any special occasion. Know someone with an upcoming birthday, anniversary, housewarming party, wedding or other event? We've got you covered!</p>
  </div>
  <div class="btn" style="left:592px;top:1765px;width:155px;height:48px">Learn More</div>

  <!-- why us -->
  <h2 class="title script" style="top:1969px">Why Us?</h2>
  <div class="abs feature-card"></div>
  <div class="feature" style="left:102px;top:2102px">
    <div class="icon" style="background:var(--green)">
      <svg width="60" height="60" viewBox="0 0 60 60" fill="none" stroke="#fff" stroke-width="2.5"><path d="M10 50l30-30 6 6-30 30H10z"/><circle cx="40" cy="42" r="8"/><path d="M14 14l14 14"/><rect x="8" y="8" width="14" height="10" rx="2"/></svg>
    </div>
    <h3>Your Idea Your Design</h3>
    <p>Each art piece is customized for you! You choose your size, orientation and art style. Makes a perfect gift!!!</p>
    <span class="readmore">Read More <span class="arrow-dot"><svg width="7" height="7" viewBox="0 0 7 7"><path d="M2 1l3 2.5L2 6" fill="none" stroke="#fff" stroke-width="1.5"/></svg></span></span>
  </div>
  <div class="feature" style="left:450px;top:2085px">
    <div class="icon" style="background:var(--orange-deep)">
      <svg width="64" height="50" viewBox="0 0 64 50" fill="none" stroke="#fff" stroke-width="2.5"><rect x="14" y="8" width="30" height="26" rx="2"/><path d="M44 16h10l6 9v9H44z"/><circle cx="24" cy="38" r="5"/><circle cx="50" cy="38" r="5"/><path d="M2 16h8M4 22h8M2 28h8"/></svg>
    </div>
    <h3>Fast Shipping</h3>
    <p>Your artwork is printed and shipped in the USA! We offer fast turnaround with transit times typically 3-7 days. Free tracking with each order!!</p>
    <span class="readmore">Read More <span class="arrow-dot"><svg width="7" height="7" viewBox="0 0 7 7"><path d="M2 1l3 2.5L2 6" fill="none" stroke="#fff" stroke-width="1.5"/></svg></span></span>
  </div>
  <div class="feature" style="left:796px;top:2084px">
    <div class="icon" style="background:var(--green)">
      <svg width="56" height="60" viewBox="0 0 56 60" fill="none" stroke="#fff" stroke-width="2.5"><circle cx="28" cy="24" r="18"/><path d="M20 24l6 6 11-12"/><path d="M16 38l-6 18 9-4 5 7 4-12M40 38l6 18-9-4-5 7-4-12"/></svg>
    </div>
    <h3>High Quality</h3>
    <p>We've put a lot of effort ensuring your artwork is of the highest quality. Each piece is printed on the highest quality, gallery grade canvas. It is ready to hang upon arrival.!</p>
    <span class="readmore">Read More <span class="arrow-dot"><svg width="7" height="7" viewBox="0 0 7 7"><path d="M2 1l3 2.5L2 6" fill="none" stroke="#fff" stroke-width="1.5"/></svg></span></span>
  </div>

  <!-- testimonials -->
  <section class="abs testimonials"></section>
  <h2 class="title script" style="top:2610px;color:#fff">Our Testimonials</h2>
  <div class="slide-arrow" style="left:108px"><svg width="12" height="14" viewBox="0 0 12 14"><path d="M8 2L3 7l5 5" fill="none" stroke="#fff" stroke-width="2"/></svg></div>
  <div class="slide-arrow" style="left:1051px"><svg width="12" height="14" viewBox="0 0 12 14"><path d="M4 2l5 5-5 5" fill="none" stroke="#fff" stroke-width="2"/></svg></div>
  <article class="review" style="left:185px">
    <h4>Marla T</h4>
    <div class="meta">Potomac, MD
      <span class="stars">
        <svg width="16" height="15" viewBox="0 0 24 23"><path d="M12 1l3.4 7 7.6 1-5.5 5.3 1.3 7.7L12 18.3 5.2 22l1.3-7.7L1 9l7.6-1z" fill="#f4a522"/></svg>
        <svg width="16" height="15" viewBox="0 0 24 23"><path d="M12 1l3.4 7 7.6 1-5.5 5.3 1.3 7.7L12 18.3 5.2 22l1.3-7.7L1 9l7.6-1z" fill="#f4a522"/></svg>
        <svg width="16" height="15" viewBox="0 0 24 23"><path d="M12 1l3.4 7 7.6 1-5.5 5.3 1.3 7.7L12 18.3 5.2 22l1.3-7.7L1 9l7.6-1z" fill="#f4a522"/></svg>
        <svg width="16" height="15" viewBox="0 0 24 23"><path d="M12 1l3.4 7 7.6 1-5.5 5.3 1.3 7.7L12 18.3 5.2 22l1.3-7.7L1 9l7.6-1z" fill="#f4a522"/></svg>
        <svg width="16" height="15" viewBox="0 0 24 23"><path d="M12 1l3.4 7 7.6 1-5.5 5.3 1.3 7.7L12 18.3 5.2 22l1.3-7.7L1 9l7.6-1z" fill="#f4a522"/></svg>
      </span>
    </div>
    <p>My mom is in an assisted living facility and has Alzheimers. We had a family portrait made into an oil and put in her room to help her remember us. The nurses always tell us how much she loves it and helps jog her memory. Thank you Brushvale Prints!</p>
  </article>
  <article class="review" style="left:608px">
    <h4>Marla T</h4>
    <div class="meta">Potomac, MD
      <span class="stars">
        <svg width="16" height="15" viewBox="0 0 24 23"><path d="M12 1l3.4 7 7.6 1-5.5 5.3 1.3 7.7L12 18.3 5.2 22l1.3-7.7L1 9l7.6-1z" fill="#f4a522"/></svg>
        <svg width="16" height="15" viewBox="0 0 24 23"><path d="M12 1l3.4 7 7.6 1-5.5 5.3 1.3 7.7L12 18.3 5.2 22l1.3-7.7L1 9l7.6-1z" fill="#f4a522"/></svg>
        <svg width="16" height="15" viewBox="0 0 24 23"><path d="M12 1l3.4 7 7.6 1-5.5 5.3 1.3 7.7L12 18.3 5.2 22l1.3-7.7L1 9l7.6-1z" fill="#f4a522"/></svg>
        <svg width="16" height="15" viewBox="0 0 24 23"><path d="M12 1l3.4 7 7.6 1-5.5 5.3 1.3 7.7L12 18.3 5.2 22l1.3-7.7L1 9l7.6-1z" fill="#f4a522"/></svg>
        <svg width="16" height="15" viewBox="0 0 24 23"><path d="M12 1l3.4 7 7.6 1-5.5 5.3 1.3 7.7L12 18.3 5.2 22l1.3-7.7L1 9l7.6-1z" fill="#f4a522"/></svg>
      </span>
    </div>
    <p>My mom is in an assisted living facility and has Alzheimers. We had a family portrait made into an oil and put in her room to help her remember us. The nurses always tell us how much she loves it and helps jog her memory. Thank you Brushvale Prints!</p>
  </article>

  <!-- gallery -->
  <h2 class="title script" style="top:3130px;line-height:43px">From Photo To Museum<br>Quality Canvas Art</h2>
  <div class="abs gallery-main" role="img" aria-label="Oil painting of a shepherd dog resting with an orange cat"></div>
  <div class="abs gallery-thumb" style="top:3250px;background:linear-gradient(160deg,#3c5a2a,#8a9a6a,#c9b896)" role="img" aria-label="Painting of a child and parent walking on a forest path"></div>
  <div class="abs gallery-thumb" style="top:3403px;background:linear-gradient(160deg,#8fb8d8,#7a3a1a,#c7dcea)" role="img" aria-label="Watercolor of a horse and rider jumping"></div>
  <div class="abs gallery-thumb" style="top:3557px;background:linear-gradient(160deg,#c96a2a,#e8e2d8,#7a8a3a)" role="img" aria-label="Painting of a puppy in autumn leaves"></div>
  <div class="btn" style="left:523px;top:3736px;width:155px;height:48px">Get Started</div>

  <!-- footer -->
  <footer class="abs footer"></footer>
  <div class="brand" style="left:113px;top:3950px;color:#fff"><span class="dot"></span>Brushvale</div>
  <span class="social" style="left:130px"></span>
  <span class="social" style="left:170px"></span>
  <span class="social" style="left:210px"></span>
  <span class="social" style="left:250px"></span>
  <div class="fcol" style="left:410px">
    <h4>Quick Links</h4>
    <ul><li>Home</li><li>Shop</li><li>Testimonials</li><li>About Us</li><li>FAQs</li><li>My Orders</li><li>Contact Us</li></ul>
  </div>
  <div class="fcol" style="left:627px">
    <h4>About Company</h4>
    <ul><li>Legal Information</li><li>Terms &amp; Condition</li><li>Privacy Policy</li><li>Support</li><li>Site Map</li></ul>
  </div>
  <div class="fcol" style="left:868px">
    <h4>Contact Us</h4>
    <div class="contact-item">
      <svg width="14" height="14" viewBox="0 0 24 24"><path d="M6 2l4 5-2 3c1.5 3 3 4.5 6 6l3-2 5 4-2 4C10 22 2 14 2 4z" fill="#1ba0d8"/></svg>
      <div><b>Phone</b>+1 888 888 8888</div>
    </div>
    <div class="contact-item">
      <svg width="14" height="12" viewBox="0 0 24 18"><rect width="24" height="18" rx="2" fill="#1ba0d8"/><path d="M2 3l10 7 10-7" fill="none" stroke="#2b2b2b" stroke-width="2"/></svg>
      <div><b>Email</b>info@brushvaleprints.com</div>
    </div>
    <div class="contact-item">
      <svg width="14" height="16" viewBox="0 0 24 30"><path d="M12 0a10 10 0 0110 10c0 8-10 20-10 20S2 18 2 10A10 10 0 0112 0z" fill="#1ba0d8"/><circle cx="12" cy="10" r="4" fill="#2b2b2b"/></svg>
      <div><b>Location</b>777 Lorem ipsum dolor sit<br>consectetur adipiscing elit,</div>
    </div>
  </div>
  <div class="abs to-top"><svg width="14" height="10" viewBox="0 0 14 10"><path d="M2 8l5-5 5 5" fill="none" stroke="#fff" stroke-width="2"/></svg></div>
  <div class="abs footer-rule"></div>
  <p class="copyright">2023 Copyright - Brushvale Prints |&nbsp; All Rights Reserved</p>

</div>
</body>
</html>
```